Velvor IT Services Business Card

Velvor IT Services are a Perth based IT Services company. We would like to incorporate our company logo (attached) and stick with the blue that is in that design. I would like a clean look design that isn't too busy, yet creates a lasting image that is instantly recognisable in the recipients mind.

Target Market(s)

The target audience is small/medium business owners.

Industry/Entity Type

Business

Font styles to use
Serif
Sans Serif

Colors

Designer to choose colors to be used in the design.

Requirements
Must have
• The design should include:
Business name: Velvor IT Services
Directors Name: Marcus Dredge
Phone Number: 0483 906 452
Email: support@velvorit.com.au
Website: www.velvorit.com.au

```html
<!DOCTYPE html>
<html lang="en">
<head>
<meta charset="utf-8">
<title>Velvor IT Services – Business Card</title>
<link rel="stylesheet" href="https://fonts.googleapis.com/css2?family=Open+Sans:wght@400;700&family=Tinos:wght@400&display=swap">
<style>
  :root {
    --backdrop: #ededed;
    --card: #ffffff;
    --card-edge: #b9b9b9;
    --brand-blue: #3b8fd6;
    --brand-deep: #1f5fae;
    --ink: #111111;
    --glass-a: #c9d3e6;
    --glass-b: #eef1f6;
  }
  * { margin: 0; padding: 0; box-sizing: border-box; }
  html, body {
    width: 1200px; height: 702px; overflow: hidden;
    background: var(--backdrop);
  }
  .canvas { position: relative; width: 1200px; height: 702px; }

  .card {
    position: absolute; left: 36px; top: 31px;
    width: 1127px; height: 639px;
    border-radius: 60px;
    background: radial-gradient(ellipse 62% 58% at 52% 45%, var(--card) 55%, #f1f1f1 78%, var(--card-edge) 100%);
    overflow: hidden;
  }

  .brand {
    position: absolute; left: 70px; top: 150px;
    display: flex; align-items: center; gap: 12px;
  }
  .brand-mark { width: 22px; height: 22px; background: var(--brand-blue); }
  .brand-name {
    font-family: "Open Sans", sans-serif; font-weight: 700;
    font-size: 30px; color: var(--brand-deep); letter-spacing: 0.5px;
  }

  .decor-glass {
    position: absolute; left: 320px; top: 50px;
    width: 640px; height: 300px;
    border-radius: 30px;
    background: linear-gradient(160deg, var(--glass-b) 0%, var(--glass-a) 45%, var(--glass-b) 75%, rgba(255,255,255,0) 100%);
    opacity: 0.75;
    transform: rotate(-14deg);
  }

  .holder {
    position: absolute; right: 91px; top: 275px; text-align: right;
  }
  .holder-name {
    font-family: "Tinos", serif; font-size: 68px; color: var(--ink);
    line-height: 1; letter-spacing: -1px;
  }
  .holder-role {
    font-family: "Open Sans", sans-serif; font-size: 32px;
    color: var(--brand-blue); line-height: 1.1; margin-top: 2px;
  }

  .contact { position: absolute; left: 73px; top: 338px; font-family: "Tinos", serif; }
  .contact-row { position: absolute; left: 0; white-space: nowrap; display: flex; align-items: baseline; }
  .contact-label { color: var(--brand-blue); width: 113px; }
  .contact-value { color: var(--ink); font-size: 30px; }
  .row-phone { top: 0; }
  .row-phone .contact-label { font-size: 33px; }
  .row-email { top: 70px; }
  .row-email .contact-label { font-size: 33px; width: 118px; }
  .row-web { top: 148px; }
  .row-web .contact-label { font-size: 28px; }
</style>
</head>
<body>
<div class="canvas">
  <div class="card">
    <div class="decor-glass" role="img" aria-label="Decorative cluster of translucent blue glass tiles"></div>

    <div class="brand">
      <span class="brand-mark"></span>
      <span class="brand-name">Velvor IT Services</span>
    </div>

    <div class="holder">
      <div class="holder-name">Marcus Dredge</div>
      <div class="holder-role">Director</div>
    </div>

    <div class="contact">
      <div class="contact-row row-phone"><span class="contact-label">Phone :</span><span class="contact-value">0483 906 452</span></div>
      <div class="contact-row row-email"><span class="contact-label">email :</span><span class="contact-value">support@velvorit.com.au</span></div>
      <div class="contact-row row-web"><span class="contact-label">website :</span><span class="contact-value">www.velvorit.com.au</span></div>
    </div>
  </div>
</div>
</body>
</html>
```